A colourful crystal mystical tapestry

I need an image for my book cover. The title of the book is A Harbour of Lanterns . Below, the subtitle is Along the Copper Road. The crystals move from bottom right to one third up the cover and into the middle. Stop below book title. (Book is 9x6). The crystals have to look like a multi-colour tapestry. Real crystals appear like they are gently exploding from the bottom right of the cover. More like movement than rocketships pls. But not a bunch of fragments. More clustered together. The upper cover will be white. They crystals are multi-covered bright - shinning. It can not be a bad AI image. It must be sharp and brilliant - a tapestry of colours. It is a spiritual book so, it needs to feel as such. If another creative idea comes to mind...give it a try.. I am open to something completely different as long as if is a multi-colour adult appealing spiritual unique image- which represents the title well. THANKS in advance.

Target Market(s)

Readers of multi-dimensional stories. ADULTS

Industry/Entity Type

Spirituality. Beautiful interesting intriguing.

Requirements
Nice to have
• It's tapestry, not chaos per say.
Should not have
• Anything crappy space like AI I can easily create. Be unique.

```html
<!DOCTYPE html>
<html lang="en">
<head>
<meta charset="utf-8">
<title>A Harbour of Lanterns — Book Cover</title>
<link rel="stylesheet" href="https://fonts.googleapis.com/css2?family=Marcellus&family=Alegreya:wght@500&display=swap">
<style>
  :root {
    --backdrop: #dcdcdc;
    --paper: #f2f2f1;
    --paper-glow: #ffffff;
    --ink-navy: #1f2450;
    --ink-plum: #4e2a66;
    --ink-magenta: #8a2f6e;
    --ink-sub: #2a2630;
    --crystal-rose: #d6405e;
    --crystal-coral: #ec6e4c;
    --crystal-amber: #f7b64c;
    --crystal-light: #fbe2a6;
    --crystal-sage: #8fc2ad;
    --crystal-teal: #2ea2b6;
    --crystal-blue: #2c6aa9;
    --crystal-violet: #5a4392;
    --crystal-night: #2a2458;
  }
  * { margin: 0; padding: 0; box-sizing: border-box; }
  html, body {
    width: 716px;
    height: 1200px;
    overflow: hidden;
    background: var(--backdrop);
  }
  .canvas {
    position: relative;
    width: 716px;
    height: 1200px;
  }
  .book-cover {
    position: absolute;
    left: 28px;
    top: 119px;
    width: 660px;
    height: 962px;
    overflow: hidden;
    background: radial-gradient(ellipse at 50% 50%, var(--paper-glow) 0%, var(--paper) 70%);
  }
  .cover-title {
    position: absolute;
    top: 58px;
    left: 0;
    width: 100%;
    text-align: center;
    font-family: "Marcellus", serif;
    line-height: 0.92;
    text-transform: uppercase;
    background: linear-gradient(100deg, var(--ink-navy) 0%, var(--ink-plum) 30%, var(--ink-magenta) 52%, var(--ink-navy) 78%, var(--ink-plum) 100%);
    -webkit-background-clip: text;
    background-clip: text;
    color: transparent;
  }
  .cover-title .title-lead { display: block; font-size: 78px; }
  .cover-title .title-line { display: block; font-size: 86px; letter-spacing: 1px; }
  .cover-subtitle {
    position: absolute;
    top: 318px;
    left: 0;
    width: 100%;
    text-align: center;
    font-family: "Alegreya", serif;
    font-weight: 500;
    font-size: 31px;
    letter-spacing: 1.5px;
    color: var(--ink-sub);
  }
  .crystal-field {
    position: absolute;
    left: 0;
    bottom: 0;
    width: 660px;
    height: 600px;
  }
</style>
</head>
<body>
  <div class="canvas">
    <section class="book-cover">
      <h1 class="cover-title">
        <span class="title-lead">A</span>
        <span class="title-line">Harbour of</span>
        <span class="title-line">Lanterns</span>
      </h1>
      <p class="cover-subtitle">Along the Copper Road</p>

      <svg class="crystal-field" viewBox="0 0 660 600" role="img" aria-label="Illustration of a tapestry of tall faceted crystals rising in a rainbow band: rose and violet crystals on the left, glowing amber crystals in the centre, teal and blue crystals on the right, with small bright shards drifting upward toward the title">
        <defs>
          <linearGradient id="crystal-hues" x1="0" y1="0" x2="1" y2="0">
            <stop offset="0" stop-color="var(--crystal-rose)"/>
            <stop offset="0.22" stop-color="var(--crystal-coral)"/>
            <stop offset="0.42" stop-color="var(--crystal-amber)"/>
            <stop offset="0.5" stop-color="var(--crystal-light)"/>
            <stop offset="0.62" stop-color="var(--crystal-sage)"/>
            <stop offset="0.8" stop-color="var(--crystal-teal)"/>
            <stop offset="1" stop-color="var(--crystal-blue)"/>
          </linearGradient>
          <linearGradient id="crystal-depth" x1="0" y1="0" x2="0" y2="1">
            <stop offset="0.3" stop-color="var(--crystal-violet)" stop-opacity="0"/>
            <stop offset="0.65" stop-color="var(--crystal-violet)" stop-opacity="0.55"/>
            <stop offset="1" stop-color="var(--crystal-night)" stop-opacity="0.95"/>
          </linearGradient>
          <linearGradient id="crystal-fade" x1="0" y1="0" x2="0" y2="1">
            <stop offset="0" stop-color="#fff" stop-opacity="1"/>
            <stop offset="0.14" stop-color="#fff" stop-opacity="0.55"/>
            <stop offset="0.3" stop-color="#fff" stop-opacity="0"/>
          </linearGradient>
          <radialGradient id="crystal-glow" cx="0.5" cy="0.32" r="0.32">
            <stop offset="0" stop-color="#fff6dc" stop-opacity="0.85"/>
            <stop offset="1" stop-color="#fff6dc" stop-opacity="0"/>
          </radialGradient>
        </defs>
        <path d="M0 40 C 150 60, 250 170, 330 190 C 420 175, 540 120, 660 70 L 660 600 L 0 600 Z" fill="url(#crystal-hues)"/>
        <path d="M0 40 C 150 60, 250 170, 330 190 C 420 175, 540 120, 660 70 L 660 600 L 0 600 Z" fill="url(#crystal-depth)"/>
        <path d="M0 40 C 150 60, 250 170, 330 190 C 420 175, 540 120, 660 70 L 660 600 L 0 600 Z" fill="url(#crystal-fade)"/>
        <rect x="0" y="0" width="660" height="600" fill="url(#crystal-glow)"/>
      </svg>
    </section>
  </div>
</body>
</html>
```